Cat Litter Package and Logo Design

We want new package and Logo design for Cat pine wood litter. Name is “OLVO”. It will be sold in pet store, online shop and supermarket. Our slogan is “Cat litter for your cat, the member of our family”. I mean that cat is not just a pet. They like people in our family. The product for cat is must be the best as selected for member of our family.

Package: Plastic bag with 2 sides
Package Dimension: width 35 cm height 50 cm

Important:
1. Customer will know immediately what product is and for.
2. Outstanding from competitors.
3. Easy to recognize the product.

Front side detail:
1. Cat image
2. Logo: Olvo
3. Slogan: Cat litter for your cat, the member of our family.
4. Detail: Pine Wood Cat Litter
5. Main Highlight -> Breeder Selected
6. Main Features -> Non-Clumping / Odor Control / Dust Free / Save Money / Eco Friendly
7. Show real product (pine wood) inside package: Area to show product will be transparent.
8. Net WT 10 L

Back side detail:
1. One bag for 1 cat & 2 months
2. Benefit: Non-Clumping / Odor Control / Dust Free / Save Money / Eco Friendly
3. How to change for using Olvo Pine Wood Litter: Please mix Olvo with the old one. When your cat can be familiar with Olvo. You can use only Olvo in your cat litter tray.
4. Direction
4.1 Fill the litter height for 2 inches.
4.2 Scoop solid waste.
4.3 Shake litter tray for urine sawdust
4.4 Maintain the height of litter for 2 inches.
5. Imported and Distribution by
5.1 QFO Tech Co.,Ltd.
5.2 Email: Quietfernowlstudio@plumbox.net
6. Little text: *Recommended to use with cat litter tray.

Attached:
1. Our competitors packages
2. Real Cat: You can use it on the package. (I have attached many images, you can select it and use for suitable way.)***
3. Cat litter tray: Don’t use this image. It’s just for describe what is cat litter tray. I prefer drawing.
4. Real product: pine wood

Note: Cat litter is for cat toilet. It's not cat's food.

Target Market(s)

Cat owners whose cats use a litter tray

Industry/Entity Type

Pet

Logo Text

OLVO

Requirements
Must have
• 1. Customer will know immediately what product is and for.
• 2. Outstanding from competitors.
• 3. Easy to recognize the product.

```html
<!DOCTYPE html>
<html lang="en">
<head>
<meta charset="utf-8">
<title>Olvo Pine Wood Cat Litter – Front Pack</title>
<link rel="stylesheet" href="https://fonts.googleapis.com/css2?family=Amatic+SC:wght@400;700&display=swap">
<style>
  :root {
    --paper-left: #e7e5d6;
    --paper-right: #f3f1e5;
    --ink: #141414;
    --teal: #7ecbbb;
    --teal-deep: #62b9ab;
    --teal-light: #9ad6c9;
    --tag-yellow: #ece4a6;
    --pine: #3a9a4a;
    --lime: #b8d83a;
    --white: #ffffff;
  }
  * { margin: 0; padding: 0; box-sizing: border-box; }
  html, body { width: 840px; height: 1200px; overflow: hidden; }
  body { font-family: "Amatic SC", "Arial Narrow", sans-serif; color: var(--ink); }

  .pack {
    position: relative;
    width: 840px;
    height: 1200px;
    background: linear-gradient(to right, var(--paper-left) 0 420px, var(--paper-right) 420px 840px);
    overflow: hidden;
  }

  .brand-name {
    position: absolute;
    left: 120px; top: 90px;
    width: 260px;
    text-align: center;
    font-size: 170px;
    font-weight: 700;
    line-height: 1;
  }

  .slogan {
    position: absolute;
    left: 452px; top: 128px;
    width: 320px;
    font-size: 44px;
    font-weight: 700;
    line-height: 0.95;
    text-align: center;
  }

  .divider {
    position: absolute;
    left: 48px; top: 328px;
    width: 744px; height: 1px;
    background: var(--ink);
  }

  .tree {
    position: absolute;
    border-radius: 4px;
    background: linear-gradient(to bottom, var(--pine) 0 85%, #8a7a3a 85%);
  }
  .tree--left { left: 200px; top: 372px; width: 82px; height: 110px; }
  .tree--right { left: 556px; top: 400px; width: 62px; height: 82px; }

  .wood-tag {
    position: absolute;
    left: 290px; top: 362px;
    width: 256px; height: 48px;
    background: var(--tag-yellow);
    clip-path: polygon(0 0, 90% 0, 100% 50%, 90% 100%, 0 100%);
    font-size: 40px;
    font-weight: 700;
    line-height: 48px;
    text-align: center;
    padding-right: 16px;
  }

  .product-type {
    position: absolute;
    left: 290px; top: 404px;
    width: 260px;
    text-align: center;
    font-size: 92px;
    font-weight: 700;
    line-height: 1;
  }

  .highlight-band {
    position: absolute;
    left: 0; top: 502px;
    width: 840px; height: 122px;
    background: linear-gradient(to bottom, var(--teal-light) 0 10%, var(--teal) 10% 88%, var(--teal-deep) 88%);
    transform: skewY(-0.4deg);
  }
  .highlight-text {
    position: absolute;
    left: 0; top: 502px;
    width: 840px; height: 122px;
    display: flex; align-items: center; justify-content: center; gap: 34px;
    color: var(--white);
    font-size: 112px;
    font-weight: 700;
    line-height: 1;
    text-shadow: 3px 3px 0 rgba(60, 120, 110, 0.45);
  }
  .highlight-text .mark { font-size: 56px; }

  .features {
    position: absolute;
    left: 0; top: 698px;
    width: 334px; height: 402px;
  }
  .features-bg {
    position: absolute; inset: 0;
    background: var(--teal-deep);
    clip-path: polygon(5% 7%, 100% 0, 96% 87%, 0 100%);
  }
  .feature-list {
    position: absolute;
    left: 48px; top: 50px;
    list-style: none;
  }
  .feature {
    display: flex; align-items: center;
    height: 64px;
    color: var(--white);
    font-size: 44px;
    font-weight: 700;
  }
  .feature::before {
    content: "";
    width: 8px; height: 8px;
    border-radius: 50%;
    background: var(--lime);
    margin-right: 12px;
  }
  .feature-name { width: 204px; }
  .feature-icon {
    width: 52px; height: 46px;
    background: var(--teal-light);
    display: flex; align-items: center; justify-content: center;
  }
  .feature-icon svg { width: 36px; height: 28px; }

  .cat-photo {
    position: absolute;
    left: 436px; top: 690px;
    width: 404px; height: 510px;
    border-radius: 46% 46% 0 0 / 30% 30% 0 0;
    background: radial-gradient(ellipse at 50% 70%, #f4ece4 0 30%, #d9a86b 55%, #b9844d 80%);
  }

  .net-weight {
    position: absolute;
    left: 302px; top: 1096px;
    width: 236px; height: 88px;
    display: flex;
    color: var(--white);
    font-weight: 700;
  }
  .net-weight-label {
    width: 116px;
    background: var(--teal-deep);
    display: flex; align-items: center; justify-content: center;
    font-size: 40px;
    text-decoration: underline;
    text-underline-offset: 4px;
  }
  .net-weight-value {
    flex: 1;
    background: var(--teal);
    display: flex; align-items: center; justify-content: center;
    font-size: 76px;
  }
</style>
</head>
<body>
<main class="pack">
  <div class="brand-name">Olvo</div>
  <p class="slogan">Cat Litter for your Cat,<br>the member of our family.</p>
  <div class="divider"></div>

  <div class="tree tree--left" role="img" aria-label="Illustrated green pine tree"></div>
  <div class="tree tree--right" role="img" aria-label="Illustrated green pine tree"></div>
  <div class="wood-tag">– Pine Wood –</div>
  <h1 class="product-type">Cat Litter</h1>

  <div class="highlight-band"></div>
  <div class="highlight-text"><span class="mark">×</span><span>Breeder Selected</span><span class="mark">×</span></div>

  <section class="features">
    <div class="features-bg"></div>
    <ul class="feature-list">
      <li class="feature"><span class="feature-name">Non-Clumping</span>
        <span class="feature-icon"><svg viewBox="0 0 36 28"><path d="M4 22 Q4 14 11 14 Q13 7 20 8 Q27 8 28 15 Q33 15 33 22 Z" fill="#fff"/></svg></span></li>
      <li class="feature"><span class="feature-name">Odor Control</span>
        <span class="feature-icon"><svg viewBox="0 0 36 28"><path d="M14 3 Q10 8 14 12 Q18 16 14 21 M21 3 Q17 8 21 12 Q25 16 21 21" stroke="#fff" stroke-width="2.5" fill="none"/><rect x="8" y="23" width="20" height="2.5" fill="#fff"/></svg></span></li>
      <li class="feature"><span class="feature-name">Dust Free</span>
        <span class="feature-icon"><svg viewBox="0 0 36 28"><circle cx="12" cy="15" r="7" fill="#fff"/><circle cx="20" cy="11" r="8" fill="#fff"/><circle cx="27" cy="16" r="6" fill="#fff"/><rect x="12" y="14" width="15" height="8" fill="#fff"/></svg></span></li>
      <li class="feature"><span class="feature-name">Save Money</span>
        <span class="feature-icon"><svg viewBox="0 0 36 28"><text x="18" y="22" text-anchor="middle" font-family="Amatic SC, sans-serif" font-weight="700" font-size="24" fill="#fff">$$$</text></svg></span></li>
      <li class="feature"><span class="feature-name">Eco Friendly</span>
        <span class="feature-icon"><svg viewBox="0 0 36 28"><ellipse cx="18" cy="13" rx="7" ry="11" fill="#fff"/><path d="M18 5 V26" stroke="#62b9ab" stroke-width="1.5"/></svg></span></li>
    </ul>
  </section>

  <div class="cat-photo" role="img" aria-label="Photo of a ginger and white cat lying down, facing forward"></div>

  <div class="net-weight">
    <span class="net-weight-label">Net Wt:</span>
    <span class="net-weight-value">10 KG</span>
  </div>
</main>
</body>
</html>
```